For lease banners for Businesses

I need to turn all of these banners into high quality graphics so I can get them printed on vinyl vertical banners that are 44"W x 88"H. So I need them most likely to be vector artwork, and ready to upload to a custom vinyl print shop.

```html
<!DOCTYPE html>
<html lang="en">
<head>
<meta charset="utf-8">
<title>For Lease Banner – Northgate Holdings</title>
<link rel="stylesheet" href="https://fonts.googleapis.com/css2?family=Montserrat:wght@500&family=Open+Sans:wght@700&family=Roboto+Condensed:wght@500;900&display=swap">
<style>
  :root {
    --ink: #050505;
    --night: #1b1c1f;
    --gold: #c9921f;
    --white: #ffffff;
    --warm-light: #8a6a3a;
    --warm-deep: #3a2c1c;
  }
  html, body {
    margin: 0;
    padding: 0;
    width: 1200px;
    height: 2323px;
    overflow: hidden;
    background: var(--ink);
  }
  .banner {
    position: relative;
    width: 1200px;
    height: 2323px;
    overflow: hidden;
    background: linear-gradient(180deg, var(--ink) 0%, #0a0a0b 25%, var(--night) 48%, #202124 100%);
  }
  .banner svg { position: absolute; left: 0; top: 0; }
  .property-photo {
    position: absolute;
    left: 0;
    top: 1000px;
    width: 1200px;
    height: 664px;
    background:
      radial-gradient(ellipse at 48% 55%, var(--warm-light) 0%, rgba(90,66,38,0.8) 30%, rgba(40,32,24,0.6) 60%, transparent 85%),
      linear-gradient(180deg, #1d1e21 0%, var(--warm-deep) 45%, #2a241e 80%, #3a3530 100%);
  }
  .brand-name {
    font-family: "Montserrat", sans-serif;
    font-weight: 500;
    fill: var(--white);
  }
  .headline {
    font-family: "Roboto Condensed", sans-serif;
    font-weight: 900;
    fill: var(--white);
  }
  .feature-label {
    font-family: "Roboto Condensed", sans-serif;
    font-weight: 500;
    font-size: 26px;
    letter-spacing: 1px;
    fill: var(--white);
  }
  .phone {
    font-family: "Roboto Condensed", sans-serif;
    font-weight: 900;
    fill: var(--white);
  }
  .email {
    font-family: "Open Sans", sans-serif;
    font-weight: 700;
    fill: var(--white);
  }
  .gold-rule { stroke: var(--gold); stroke-width: 3; }
  .icon { fill: none; stroke: var(--gold); stroke-width: 3; stroke-linejoin: round; stroke-linecap: round; }
</style>
</head>
<body>
<main class="banner">
  <div class="property-photo" role="img" aria-label="Night photograph of a modern brick commercial building with large lit glass storefront windows, sidewalk and landscaping"></div>

  <svg width="1200" height="2323" viewBox="0 0 1200 2323" xmlns="http://www.w3.org/2000/svg">
    <!-- brand -->
    <g class="brand">
      <rect x="200" y="140" width="202" height="212" fill="none" stroke="var(--gold)" stroke-width="4"/>
      <text class="brand-name" x="473" y="283" font-size="98" textLength="594" lengthAdjust="spacingAndGlyphs">NORTHGATE</text>
      <text class="brand-name" x="473" y="335" font-size="46" textLength="594" lengthAdjust="spacing">HOLDINGS</text>
    </g>
    <line class="gold-rule" x1="85" y1="396" x2="1110" y2="396"/>

    <!-- headline -->
    <text class="headline" x="257" y="768" font-size="448" textLength="704" lengthAdjust="spacingAndGlyphs">FOR</text>
    <text class="headline" x="124" y="1098" font-size="424" textLength="992" lengthAdjust="spacingAndGlyphs">LEASE</text>

    <!-- features -->
    <rect x="0" y="1664" width="1200" height="188" fill="var(--ink)"/>
    <line class="gold-rule" x1="0" y1="1664" x2="1200" y2="1664"/>
    <line class="gold-rule" x1="411" y1="1690" x2="411" y2="1823" stroke-width="2"/>
    <line class="gold-rule" x1="810" y1="1690" x2="810" y2="1823" stroke-width="2"/>

    <g class="icon">
      <!-- building -->
      <rect x="174" y="1712" width="38" height="58"/>
      <rect x="212" y="1686" width="34" height="84"/>
      <rect x="246" y="1700" width="32" height="70"/>
      <path d="M182 1724h8M196 1724h8M182 1738h8M196 1738h8M182 1752h8M196 1752h8M222 1698v60M236 1698v60M256 1712v50M268 1712v50"/>
      <!-- handshake -->
      <path d="M548 1704l22-12 26 10 26-10 22 12 8 22-14 12-26 20-20 4-16-14-24-20z"/>
      <path d="M596 1702l-18 16 8 8 22-12 30 28M578 1742l10 10M588 1734l12 12"/>
      <!-- people -->
      <circle cx="946" cy="1708" r="13"/>
      <circle cx="913" cy="1714" r="10"/>
      <circle cx="979" cy="1714" r="10"/>
      <path d="M916 1768v-14a30 24 0 0 1 60 0v14z"/>
      <path d="M893 1760v-10a20 18 0 0 1 26-16M999 1760v-10a20 18 0 0 0-26-16"/>
    </g>

    <text class="feature-label" x="221" y="1823" text-anchor="middle">COMMERCIAL SPACE</text>
    <text class="feature-label" x="609" y="1823" text-anchor="middle">FLEXIBLE OPPORTUNITY</text>
    <text class="feature-label" x="1000" y="1823" text-anchor="middle">LOCALLY OWNED</text>

    <line class="gold-rule" x1="0" y1="1852" x2="1200" y2="1852"/>

    <!-- contact -->
    <rect x="0" y="1854" width="1200" height="443" fill="var(--ink)"/>
    <text class="phone" x="81" y="2062" font-size="212" textLength="1047" lengthAdjust="spacingAndGlyphs">555-014-2290</text>
    <line class="gold-rule" x1="85" y1="2113" x2="566" y2="2113"/>
    <line class="gold-rule" x1="628" y1="2113" x2="1110" y2="2113"/>
    <rect x="585" y="2101" width="24" height="24" fill="var(--gold)" transform="rotate(45 597 2113)"/>
    <text class="email" x="102" y="2201" font-size="60" textLength="1020" lengthAdjust="spacingAndGlyphs">leasing@northgateholdings.com</text>

    <rect x="0" y="2297" width="1200" height="26" fill="var(--gold)"/>
  </svg>
</main>
</body>
</html>
```